Etiketten für Wein
Zielgruppe
Weinkellerei aus Baden (Deutschland) mit Fokus im Lebensmittelhandel in Deutschland
Zielgruppe: Discount-Kunden, Männlich/Weiblich, Alter: 25-60 Jahre, wird für unter € 4,-/Fl. verkauft.
Aufgabenstellung
Wir suchen ein Frontetikett für einen Riesling aus Rheinhessen. Das Etikett sollte zeitlos, schlicht, modern anmutend sein. Hochwertiges Etikettenpapier (zweiteilig).
Weinbeschreibung:
Aussehen: helles gelb,
Geruch: Frische Frucht, heimische und exotische Früchte,
Geschmack: Feines Spiel von Frucht und animierender Säure
Anforderungen Etikett:
Maße: Höhe max. 120mm/Breite max. 80mm (darf auch kleiner oder quadratisch sein)
SK Etikett, Naturstruktur bis 90g (m²) (gerne zweiteilig)
Eine figürliche Etikettenkontur ist möglich, es wird aber am rechten Etikettenrand eine gerade Spendekante benötigt um das Etikett maschinell verarbeiten zu können.
Als Flasche wird eine 0,75 L Schlegelflasche (Farbe: feuille morte) eingesetzt.
Verschluss: Longcap
Mögliche Veredelungen: Quelllack, Prägungen, Heissfolie, Glanzlack
Pflichtangaben:
- Rheinhessen
- Auerbacher Lindenhang Riesling Qualitätswein trocken (Rebsorte 'Riesling' gerne prominent darstellen)
- Jahrgang 2023
SK Etikett, Naturstruktur bis 90g (m²) (gerne zweiteilig - einteilig aber auch möglich)

```html
<!DOCTYPE html>
<html lang="de">
<head>
<meta charset="utf-8">
<title>Riesling Etiketten – Auerbacher Lindenhang</title>
<link rel="stylesheet" href="https://fonts.googleapis.com/css2?family=Open+Sans:wght@400&family=Tenor+Sans&family=Cormorant+Garamond:wght@500&display=swap">
<style>
  :root {
    --page: #ffffff;
    --gold: #b39d7c;
    --gold-light: #d6c3a2;
    --slate-label: #4b5256;
    --slate-glass: #2e2f31;
    --slate-sleeve: #4f5659;
    --olive-label: #656a55;
    --olive-glass: #8f8f6d;
    --olive-sleeve-a: #7b8462;
    --olive-sleeve-b: #b3bb6b;
    --pearl-label: #dcdddb;
    --pearl-glass: #f7f7f6;
    --pearl-edge: #e6e7e5;
    --pearl-sleeve: #dedfdd;
    --pearl-ink: #5b5e60;
  }
  * { margin: 0; padding: 0; box-sizing: border-box; }
  html, body { width: 1163px; height: 1200px; overflow: hidden; background: var(--page); }
  .range { position: relative; width: 1163px; height: 1200px; }

  .variant { position: absolute; top: 0; width: 216px; height: 1080px; }
  .variant--slate { left: 87px; }
  .variant--olive { left: 465px; }
  .variant--pearl { left: 828px; }

  .neck-sleeve {
    position: absolute; left: 60px; top: 64px; width: 104px; height: 228px;
    display: flex; align-items: flex-end; justify-content: flex-start;
    padding: 0 0 22px 25px;
  }
  .neck-sleeve__name {
    writing-mode: vertical-rl; transform: rotate(180deg);
    font-family: "Open Sans", sans-serif; font-size: 7px; letter-spacing: 0.5px;
    color: var(--gold-light); white-space: nowrap;
  }
  .variant--slate .neck-sleeve { background: var(--slate-sleeve); }
  .variant--olive .neck-sleeve { background: linear-gradient(90deg, var(--olive-sleeve-a), var(--olive-sleeve-b)); }
  .variant--pearl .neck-sleeve { background: var(--pearl-sleeve); }
  .variant--pearl .neck-sleeve__name { color: var(--pearl-ink); }

  .front-label {
    position: absolute; left: 0; top: 776px; width: 214px; height: 294px; overflow: hidden;
  }
  .variant--slate .front-label { background: var(--slate-label); }
  .variant--olive .front-label { background: var(--olive-label); }
  .variant--pearl .front-label { background: var(--pearl-label); }

  .front-label__glass { position: absolute; left: 0; top: 0; width: 86px; height: 294px; }
  .variant--slate .front-label__glass { background: var(--slate-glass); }
  .variant--olive .front-label__glass { background: var(--olive-glass); }
  .variant--pearl .front-label__glass { background: var(--pearl-glass); border: 2px solid var(--pearl-edge); }

  .front-label__estate {
    position: absolute; left: 28px; top: 55px; width: 180px;
    font-family: "Open Sans", sans-serif; font-size: 10px; letter-spacing: 0.8px;
    color: var(--gold-light); white-space: nowrap;
  }
  .variant--pearl .front-label__estate { color: var(--pearl-ink); }
  .front-label__swash { position: absolute; left: 24px; top: 70px; width: 176px; height: 14px; }

  .front-label__variety {
    position: absolute; left: 92px; top: 177px; width: 116px; text-align: center;
    font-family: "Tenor Sans", sans-serif; font-weight: 400; font-size: 20px; letter-spacing: 1px;
    color: var(--gold); white-space: nowrap;
  }
  .front-label__details {
    position: absolute; left: 100px; top: 218px; width: 96px; text-align: center;
    font-family: "Cormorant Garamond", serif; font-weight: 500; font-size: 7px;
    line-height: 11px; letter-spacing: 0.3px; color: var(--gold);
  }
  .front-label__vintage { margin-top: 9px; font-size: 8px; }
</style>
</head>
<body>
<main class="range">

  <section class="variant variant--slate">
    <div class="neck-sleeve"><span class="neck-sleeve__name">AUERBACHER LINDENHANG</span></div>
    <article class="front-label">
      <div class="front-label__glass" role="img" aria-label="Silhouette eines Weinglases"></div>
      <p class="front-label__estate">AUERBACHER LINDENHANG</p>
      <svg class="front-label__swash" viewBox="0 0 176 14"><path d="M2 11 Q88 2 174 8" fill="none" stroke="var(--gold)" stroke-width="1.6"/></svg>
      <h2 class="front-label__variety">RIESLING</h2>
      <div class="front-label__details">
        <p>RHEINHESSEN</p><p>QUALITÄTSWEIN</p><p>TROCKEN</p>
        <p class="front-label__vintage">2023</p>
      </div>
    </article>
  </section>

  <section class="variant variant--olive">
    <div class="neck-sleeve"><span class="neck-sleeve__name">AUERBACHER LINDENHANG</span></div>
    <article class="front-label">
      <div class="front-label__glass" role="img" aria-label="Silhouette eines Weinglases"></div>
      <p class="front-label__estate">AUERBACHER LINDENHANG</p>
      <svg class="front-label__swash" viewBox="0 0 176 14"><path d="M2 11 Q88 2 174 8" fill="none" stroke="var(--gold)" stroke-width="1.6"/></svg>
      <h2 class="front-label__variety">RIESLING</h2>
      <div class="front-label__details">
        <p>RHEINHESSEN</p><p>QUALITÄTSWEIN</p><p>TROCKEN</p>
        <p class="front-label__vintage">2023</p>
      </div>
    </article>
  </section>

  <section class="variant variant--pearl">
    <div class="neck-sleeve"><span class="neck-sleeve__name">AUERBACHER LINDENHANG</span></div>
    <article class="front-label">
      <div class="front-label__glass" role="img" aria-label="Silhouette eines Weinglases"></div>
      <p class="front-label__estate">AUERBACHER LINDENHANG</p>
      <svg class="front-label__swash" viewBox="0 0 176 14"><path d="M2 11 Q88 2 174 8" fill="none" stroke="var(--gold)" stroke-width="1.6"/></svg>
      <h2 class="front-label__variety">RIESLING</h2>
      <div class="front-label__details">
        <p>RHEINHESSEN</p><p>QUALITÄTSWEIN</p><p>TROCKEN</p>
        <p class="front-label__vintage">2023</p>
      </div>
    </article>
  </section>

</main>
</body>
</html>
```